Fahrzeugbeschriftung für Fahrschule gesucht
Ich bin sehr sehr zufrieden mit dem Ergebnis.Die wünsche die ich hatte wurden ohne zu zögern gleich umgesetzt. Der Designer arbeitet schnell und Präzise. Sehr gerne wieder für zukünftige Projekte!!
Zielgruppe
Meine Firma ist eine Fahrschule. Name der Fahrschule ist ZACK. Die Fahrschule befindet sich in Heidelberg am Neckar. Wir bilden alle Motorradklassen, PKW Klassen und Anhänger für PKW aus.
Unsere Zielgruppe sind hauptsächlich Jugendliche von 16-25 Jahren.
Aufgabenstellung
Unsere Fahrzeuge sind Schwarz, der Anhänger soll als Werbefläche für die Fahrschule dienen und soll auffallen. Das Grundelement des Designs sollte eher dunkel bleiben. Der Anhänger ist weiß und soll schwarz foliert bzw. Eure Ideen soll auf die Folie drauf und das auf den Anhänger.Ich bin Motorrad begeistert und brenne für meinen Job.
Ich möchte gerne mein Logo in Illustrationen einbauen. Das Logo soll bitte auch im Grafitti Stil sein
Hier ein link als Beispiele
https://www.bildquellora.com/de/grafiken/graffiti-hintergrund?sort=best&mediatype=illustration&assetfiletype=eps&phrase=Graffiti%20Hintergrund

```html
<!DOCTYPE html>
<html lang="de">
<head>
<meta charset="utf-8">
<title>Fahrschule ZACK – Anhängerbeschriftung</title>
<link rel="stylesheet" href="https://fonts.googleapis.com/css2?family=Roboto+Condensed:ital,wght@0,700;1,700&display=swap">
<style>
  :root {
    --stage: #e9e9e7;
    --panel: #ffffff;
    --orange: #f08a24;
    --orange-deep: #e77b14;
    --ink: #111111;
  }
  * { box-sizing: border-box; margin: 0; padding: 0; }
  html, body {
    width: 1200px; height: 790px; overflow: hidden;
    background: var(--stage);
    font-family: "Roboto Condensed", "Arial Narrow", sans-serif;
  }
  .trailer-panel {
    position: absolute; left: 280px; top: 15px;
    width: 640px; height: 760px;
    background: var(--panel);
    overflow: hidden;
    box-shadow: 0 2px 10px rgba(0,0,0,.15);
  }
  .header-band { position: absolute; left: 0; top: 0; width: 640px; height: 200px; }
  .brand {
    position: absolute; left: 0; right: 0; top: 170px;
    display: flex; justify-content: center; align-items: center; gap: 12px;
  }
  .brand-square { width: 20px; height: 20px; background: var(--ink); flex: none; }
  .brand-name {
    color: var(--ink); font-size: 32px; font-weight: 700; font-style: normal;
    line-height: 1; white-space: nowrap;
  }
  .benefits { position: absolute; left: 14px; top: 268px; list-style: none; }
  .benefit { display: flex; align-items: center; height: 75px; }
  .benefit-tick { width: 80px; height: 62px; flex: none; }
  .benefit-text {
    margin-left: 14px; font-size: 33px; font-weight: 700; font-style: italic;
    color: var(--ink); letter-spacing: -0.3px; white-space: nowrap;
  }
  .contact {
    position: absolute; left: 0; right: 0; top: 512px; text-align: center;
    font-weight: 700; font-style: italic; color: var(--ink);
  }
  .contact-call { font-size: 38px; line-height: 54px; }
  .contact-line { font-size: 34px; line-height: 53px; }
  .website {
    position: absolute; left: 0; right: 0; top: 710px; text-align: center;
    color: var(--orange); font-size: 28px; font-weight: 700; font-style: italic;
  }
</style>
</head>
<body>
  <main class="trailer-panel">
    <svg class="header-band" viewBox="0 0 640 200" role="img" aria-label="Orangefarbenes Karomuster als Kopfband">
      <defs>
        <linearGradient id="band-fill" x1="0" y1="0" x2="1" y2="1">
          <stop offset="0" stop-color="#e77b14"/>
          <stop offset="1" stop-color="#f08a24"/>
        </linearGradient>
      </defs>
      <path d="M0 0 H640 V100 C470 95 260 120 0 180 Z" fill="url(#band-fill)"/>
    </svg>

    <header class="brand">
      <span class="brand-square"></span>
      <span class="brand-name">Fahrschule Zack Heidelberg</span>
    </header>

    <ul class="benefits">
      <li class="benefit">
        <svg class="benefit-tick" viewBox="0 0 80 62"><path d="M0 32 L18 26 L34 40 L78 0 L76 20 L34 62 Z" fill="#f08a24"/></svg>
        <span class="benefit-text">7 TAGE THEORIE INTENSIVKURS</span>
      </li>
      <li class="benefit">
        <svg class="benefit-tick" viewBox="0 0 80 62"><path d="M0 32 L18 26 L34 40 L78 0 L76 20 L34 62 Z" fill="#f08a24"/></svg>
        <span class="benefit-text">TOP FAHRZEUGE</span>
      </li>
      <li class="benefit">
        <svg class="benefit-tick" viewBox="0 0 80 62"><path d="M0 32 L18 26 L34 40 L78 0 L76 20 L34 62 Z" fill="#f08a24"/></svg>
        <span class="benefit-text">UNTERRICHT AUF ENGLISCH MÖGLICH</span>
      </li>
    </ul>

    <section class="contact">
      <p class="contact-call">RUF UNS AN!</p>
      <p class="contact-line">Mobil: 0176-42 917 58</p>
      <p class="contact-line">Tel.: 06221-473 915</p>
    </section>

    <p class="website">WWW.FAHRSCHULE-ZACK.DE</p>
  </main>
</body>
</html>
```